Law Offices business card

Hi there, I'll need business card for the Law Offices of Tobin Haskell. The information must convey his strategic approach and quick resolution to complex business litigation needs. Please emphasize Civil Litigation, Corporate Law, Business Governance and Real Estate Law. Tobin has over 25 years of experience in these fields.The card should be modern and edgy and the message should be clear. Please consult his current website for ideas.

Business

```html
<!DOCTYPE html>
<html lang="en">
<head>
<meta charset="utf-8">
<title>Law Offices of Tobin Haskell – Business Card</title>
<link rel="stylesheet" href="https://fonts.googleapis.com/css2?family=Tinos&family=Noto+Sans&display=swap">
<style>
  :root {
    --backdrop: #d4d4d4;
    --card: #ffffff;
    --ink: #000000;
    --rule: #1a1a1a;
    --bullet: #555555;
  }
  * { margin: 0; padding: 0; box-sizing: border-box; }
  html, body { width: 1189px; height: 1200px; overflow: hidden; }
  body { background: var(--backdrop); position: relative; color: var(--ink); }

  .card {
    position: absolute;
    left: 140px;
    width: 917px;
    height: 524px;
    background: var(--card);
    box-shadow: 0 4px 10px rgba(0,0,0,0.18);
  }
  .card--front { top: 45px; }
  .card--back  { top: 623px; }

  .serif { font-family: "Tinos", "Times New Roman", serif; }
  .sans  { font-family: "Noto Sans", Verdana, sans-serif; }

  .abs { position: absolute; line-height: 1; white-space: nowrap; }

  .holder-name { left: 72px; top: 63px; font-size: 46px; }
  .holder-title { left: 73px; top: 118px; font-size: 26px; }
  .firm-name { left: 72px; top: 195px; font-size: 39px; }

  .contact { left: 72px; display: flex; align-items: center; gap: 24px; font-size: 24.5px; }
  .contact svg { width: 22px; height: 22px; flex: none; }
  .contact--phone  { top: 290px; }
  .contact--mobile { top: 331px; }
  .contact--web    { top: 374px; }
  .contact--mail   { top: 414px; }
  .contact--place  { top: 455px; }

  .section-rule { position: absolute; top: 80px; height: 2px; background: var(--rule); }
  .section-rule--left  { left: 0; width: 311px; }
  .section-rule--right { left: 589px; right: 0; }
  .section-title { left: 0; right: 0; top: 50px; text-align: center; font-size: 66px; }

  .service { left: 282px; display: flex; align-items: center; gap: 19px; font-size: 29px; }
  .service svg { width: 14px; height: 14px; flex: none; }
  .service--civil     { top: 205px; }
  .service--corporate { top: 262px; }
  .service--estate    { top: 323px; }
  .service--governance{ top: 380px; }
</style>
</head>
<body>

<section class="card card--front">
  <h1 class="abs serif holder-name" style="font-weight:400">Tobin Haskell</h1>
  <p class="abs sans holder-title">Attorney</p>
  <h2 class="abs serif firm-name" style="font-weight:400">Law Offices of Tobin Haskell,P.A.</h2>

  <div class="abs sans contact contact--phone">
    <svg viewBox="0 0 22 22" aria-hidden="true"><rect width="22" height="22" fill="#000"/><path d="M6 4.5c1-.8 2-.6 2.4.2l1.2 2.4c.3.6 0 1.2-.5 1.5l-.8.5c.6 1.8 1.8 3.4 3.4 4.5l.7-.6c.5-.4 1.2-.4 1.6.1l1.7 2c.5.6.3 1.4-.4 1.9-1.5 1-3.2.8-5.2-.9C7.7 14.3 5.6 11 5 8.2c-.3-1.6.1-2.9 1-3.7z" fill="#fff"/></svg>
    <span>561-555-0142</span>
  </div>
  <div class="abs sans contact contact--mobile">
    <svg viewBox="0 0 22 22" aria-hidden="true"><rect width="22" height="22" fill="#000"/><rect x="7" y="3.5" width="8" height="15" rx="1" fill="#fff"/><rect x="8.3" y="5" width="5.4" height="4.5" fill="#000"/><path d="M8.6 11.5h1v1h-1zM10.5 11.5h1v1h-1zM12.4 11.5h1v1h-1zM8.6 13.6h1v1h-1zM10.5 13.6h1v1h-1zM12.4 13.6h1v1h-1zM8.6 15.7h1v1h-1zM10.5 15.7h1v1h-1zM12.4 15.7h1v1h-1z" fill="#000"/></svg>
    <span>561-555-0187</span>
  </div>
  <div class="abs sans contact contact--web">
    <svg viewBox="0 0 22 22" aria-hidden="true"><rect width="22" height="22" fill="#000"/><circle cx="11" cy="11" r="7" fill="none" stroke="#fff" stroke-width="1.6"/><ellipse cx="11" cy="11" rx="3" ry="7" fill="none" stroke="#fff" stroke-width="1.3"/><path d="M4 11h14" stroke="#fff" stroke-width="1.3"/></svg>
    <span>www.tobinhaskell-law.com</span>
  </div>
  <div class="abs sans contact contact--mail">
    <svg viewBox="0 0 22 22" aria-hidden="true"><rect width="22" height="22" fill="#000"/><rect x="4" y="6" width="14" height="10" fill="#fff"/><path d="M4 6l7 6 7-6M4 16l5-5M18 16l-5-5" fill="none" stroke="#000" stroke-width="1.2"/></svg>
    <span>tobin@tobinhaskell-law.com</span>
  </div>
  <div class="abs sans contact contact--place">
    <svg viewBox="0 0 22 22" aria-hidden="true"><rect width="22" height="22" fill="#000"/><path d="M11 18c-3-3.6-4.5-6-4.5-8a4.5 4.5 0 0 1 9 0c0 2-1.5 4.4-4.5 8z" fill="#fff"/><circle cx="11" cy="10" r="1.6" fill="#000"/></svg>
    <span>118B Harbor Lane Palm Cove,Florida 33410</span>
  </div>
</section>

<section class="card card--back">
  <div class="section-rule section-rule--left"></div>
  <h2 class="abs serif section-title" style="font-weight:400">Service</h2>
  <div class="section-rule section-rule--right"></div>

  <ul style="list-style:none">
    <li class="abs sans service service--civil">
      <svg viewBox="0 0 14 14" aria-hidden="true"><circle cx="7" cy="7" r="4.5" fill="none" stroke="var(--bullet)" stroke-width="1"/><circle cx="7" cy="7" r="2" fill="#000"/><path d="M0 7h2.5M11.5 7H14M7 0v2.5M7 11.5V14" stroke="var(--bullet)" stroke-width="1"/></svg>
      <span>Civil Litigation</span>
    </li>
    <li class="abs sans service service--corporate">
      <svg viewBox="0 0 14 14" aria-hidden="true"><circle cx="7" cy="7" r="4.5" fill="none" stroke="var(--bullet)" stroke-width="1"/><circle cx="7" cy="7" r="2" fill="#000"/><path d="M0 7h2.5M11.5 7H14M7 0v2.5M7 11.5V14" stroke="var(--bullet)" stroke-width="1"/></svg>
      <span>Corporate Law</span>
    </li>
    <li class="abs sans service service--estate">
      <svg viewBox="0 0 14 14" aria-hidden="true"><circle cx="7" cy="7" r="4.5" fill="none" stroke="var(--bullet)" stroke-width="1"/><circle cx="7" cy="7" r="2" fill="#000"/><path d="M0 7h2.5M11.5 7H14M7 0v2.5M7 11.5V14" stroke="var(--bullet)" stroke-width="1"/></svg>
      <span>Real Estate Law</span>
    </li>
    <li class="abs sans service service--governance">
      <svg viewBox="0 0 14 14" aria-hidden="true"><circle cx="7" cy="7" r="4.5" fill="none" stroke="var(--bullet)" stroke-width="1"/><circle cx="7" cy="7" r="2" fill="#000"/><path d="M0 7h2.5M11.5 7H14M7 0v2.5M7 11.5V14" stroke="var(--bullet)" stroke-width="1"/></svg>
      <span>Business Governance</span>
    </li>
  </ul>
</section>

</body>
</html>
```